Bright Harbor Counseling Letterhead for hip modern business

I would like some ombre use of the colors in the logo hip letterhead that incorporates logo colors and feel, needs to connect with young professionals and college students. i need to be able to write letters to schools to excuse absences as well. i like color blocks on one side preferably using colors from the attached logo design.

Target Market(s)

high income young people, young adults and college students

Industry/Entity Type

mental health

Font styles to use
Serif
Sans Serif

Colors
0054AA
0677BA
7BADD7
CADEEF
E8F1F8
0094D4
00A9DD
6FCCEA
C7EBF8
E9F6FB
00AB8E
00BBA5
67D7C9
C6EFE9
E9F9F6
59FF00
82FF00
B8FF75
E3FFCB
F4FFEA
A7469A
B969AE
D3A5CF
EDDBEB
F8F0F9
6B429C
8869AF
B7A5CE
E3DAEB
F3F0F8

Requirements
Must have
• a modern hip feel, somewhat color

```html
<!DOCTYPE html>
<html lang="en">
<head>
<meta charset="utf-8">
<title>Bright Harbor Counseling Letterhead</title>
<link rel="stylesheet" href="https://fonts.googleapis.com/css2?family=Josefin+Sans:wght@300&display=swap">
<style>
  :root {
    --backdrop: #ececec;
    --paper: #ffffff;
    --band-purple: #7e57ac;
    --accent-cool: #5fa8d6;
    --accent-warm: #a86aae;
    --accent-dot: #8869af;
    --ink: #333333;
  }

  html, body {
    margin: 0;
    padding: 0;
    width: 1200px;
    height: 800px;
    overflow: hidden;
    background: var(--backdrop);
  }

  .canvas {
    position: relative;
    width: 1200px;
    height: 800px;
  }

  .letterhead {
    position: absolute;
    left: 314px;
    top: 30px;
    width: 572px;
    height: 740px;
    background: var(--paper);
    box-shadow: 0 2px 10px rgba(0, 0, 0, 0.12);
  }

  .side-band {
    position: absolute;
    top: 0;
    left: 17px;
    width: 22px;
    height: 100%;
    background: var(--band-purple);
  }

  .side-accent {
    position: absolute;
    left: 0;
    top: 459px;
    width: 17px;
    height: 186px;
    background: linear-gradient(180deg, var(--accent-cool), var(--accent-warm));
  }

  .brand {
    position: absolute;
    top: 78px;
    right: 40px;
    display: flex;
    align-items: flex-start;
    gap: 6px;
  }

  .brand-name {
    font-family: "Josefin Sans", sans-serif;
    font-weight: 300;
    color: var(--ink);
    text-align: right;
    line-height: 1;
    margin: 14px 0 0;
  }

  .brand-name .line-main {
    display: block;
    font-size: 20px;
  }

  .brand-name .line-sub {
    display: block;
    font-size: 10px;
    letter-spacing: 1.5px;
    margin-top: 4px;
  }

  .brand-dot {
    flex: none;
  }
</style>
</head>
<body>
  <main class="canvas">
    <section class="letterhead">
      <div class="side-band"></div>
      <div class="side-accent" role="img" aria-label="Decorative colour accent along the left edge"></div>
      <header class="brand">
        <p class="brand-name">
          <span class="line-main">Bright Harbor</span>
          <span class="line-sub">Counseling</span>
        </p>
        <svg class="brand-dot" width="26" height="26" viewBox="0 0 26 26" aria-hidden="true">
          <circle cx="13" cy="13" r="12" fill="var(--accent-dot)"/>
        </svg>
      </header>
    </section>
  </main>
</body>
</html>
```